Hvac and insulation company needs good looking business card design

We are hvac and insulation company and looking for a new business cards that look to today standards designs

Target Market(s)

homeowners

Industry/Entity Type

Hvac

Contact Information for Business Card

Name: Dorian Velkova
Home comfort consultant
address: 4827 Marrow Ridge Rd #215 Oakland, CA 94611
office: 888-317-5069
cell: 510-642-1388
Lic.# 458127
Email: dorian@quarry-hvac.com
Web: quarry-hvac.com

Requirements
Must have
• clean and sleek look
Nice to have
• simple with a clean look
Should not have
• to busy business card

```html
<!DOCTYPE html>
<html lang="en">
<head>
<meta charset="utf-8">
<title>Quarry Home Solutions – Business Card</title>
<link rel="stylesheet" href="https://fonts.googleapis.com/css2?family=Open+Sans:ital,wght@0,400;0,600;0,700;1,600&display=swap">
<style>
  :root {
    --stage: #2b2b2c;
    --stage-dark: #1a1a1b;
    --card: #232323;
    --card-edge: #2a2a2a;
    --orange: #f0900f;
    --text: #e6e6e6;
    --muted: #9a9a9a;
  }
  * { box-sizing: border-box; margin: 0; padding: 0; }
  html, body { width: 1200px; height: 900px; overflow: hidden; }
  body {
    background: radial-gradient(ellipse at 60% 20%, var(--stage) 0%, var(--stage-dark) 80%);
    font-family: "Open Sans", Arial, sans-serif;
    color: var(--text);
    position: relative;
  }
  .card {
    position: absolute;
    left: 260px;
    width: 680px;
    height: 388px;
    background: var(--card);
    border: 1px solid var(--card-edge);
    box-shadow: 0 18px 40px rgba(0,0,0,0.55);
  }
  .card--front { top: 46px; }
  .card--back { top: 466px; }

  .wordmark {
    position: absolute;
    display: flex;
    align-items: center;
    gap: 14px;
    color: var(--orange);
    font-weight: 700;
    letter-spacing: 1px;
    line-height: 1;
  }
  .wordmark__square {
    width: 0.62em;
    height: 0.62em;
    background: var(--orange);
  }
  .card--front .wordmark {
    font-size: 64px;
    left: 50%;
    top: 150px;
    transform: translateX(-50%);
  }
  .card--back .wordmark {
    font-size: 50px;
    right: 44px;
    top: 90px;
  }
  .site-link {
    position: absolute;
    left: 0; right: 0;
    bottom: 36px;
    text-align: center;
    font-size: 17px;
    letter-spacing: 1px;
    color: var(--text);
  }
  .site-link__domain { color: var(--orange); }

  .person {
    position: absolute;
    left: 44px;
    top: 38px;
  }
  .person__name {
    font-size: 30px;
    font-weight: 700;
    color: #ffffff;
    letter-spacing: 1.5px;
  }
  .person__role {
    font-size: 16px;
    font-weight: 600;
    font-style: italic;
    color: var(--orange);
    margin-top: -2px;
    letter-spacing: 0.5px;
  }

  .contacts {
    position: absolute;
    left: 44px;
    bottom: 40px;
    list-style: none;
    font-size: 17px;
    line-height: 29px;
  }
  .contacts li { display: flex; align-items: center; gap: 16px; }
  .contacts svg { width: 18px; height: 18px; flex: none; }
  .contacts__domain { color: var(--orange); }

  .office {
    position: absolute;
    right: 44px;
    bottom: 40px;
    text-align: right;
    font-size: 19px;
    line-height: 27px;
    letter-spacing: 1px;
  }
  .office__lic-label { color: var(--orange); }
</style>
</head>
<body>

  <section class="card card--front" aria-label="Card front">
    <div class="wordmark"><span class="wordmark__square"></span>quarry</div>
    <p class="site-link">www.<span class="site-link__domain">quarry-hvac</span>.com</p>
  </section>

  <section class="card card--back" aria-label="Card back">
    <div class="person">
      <h1 class="person__name">Dorian Velkova</h1>
      <p class="person__role">Home comfort consultant</p>
    </div>

    <div class="wordmark"><span class="wordmark__square"></span>quarry</div>

    <ul class="contacts">
      <li>
        <svg viewBox="0 0 18 18" fill="none" stroke="var(--orange)" stroke-width="1.6"><rect x="5" y="1.5" width="8" height="15" rx="1.5"/><line x1="8" y1="13.5" x2="10" y2="13.5"/></svg>
        888-317-5069
      </li>
      <li>
        <svg viewBox="0 0 18 18" fill="var(--orange)"><path d="M4 2l3 3-1.5 2a9 9 0 0 0 5.5 5.5L13 11l3 3-2 2.2C8 15.5 2.5 10 1.8 4z"/></svg>
        510-642-1388
      </li>
      <li>
        <svg viewBox="0 0 18 18" fill="none" stroke="var(--orange)" stroke-width="1.6"><rect x="1.5" y="4" width="15" height="10"/><path d="M1.5 4l7.5 6 7.5-6"/></svg>
        dorian@quarry-hvac.com
      </li>
      <li>
        <svg viewBox="0 0 18 18" fill="none" stroke="var(--orange)" stroke-width="1.4"><circle cx="9" cy="9" r="7.5"/><ellipse cx="9" cy="9" rx="3.5" ry="7.5"/><line x1="1.5" y1="9" x2="16.5" y2="9"/><line x1="3" y1="5" x2="15" y2="5"/><line x1="3" y1="13" x2="15" y2="13"/></svg>
        <span>www.<span class="contacts__domain">quarry-hvac</span>.com</span>
      </li>
    </ul>

    <address class="office" style="font-style: normal;">
      <span class="office__lic-label">Lic#</span>458127<br>
      4827 Marrow Ridge Rd #215<br>
      Oakland, CA 94611
    </address>
  </section>

</body>
</html>
```